Small business updating business cards

We have already updated our logo via Pixel Forum and downloaded it (hopefully) for you to use. Now an updated set of business cards for Neil Pollard and Stuart Pollard are also needed... we are also hoping that a copy of our outdated business card designs have uploaded successfully as Microsoft Publisher files. Our Strength Through Unity motto has died a slow death so we are hoping to remove it (and other superfluous lingo if the graphic covers the idea) and instead opt for a fancy graphic (?) on the second side of the card that really reflects our desire to obtain product / haulage from Road Transport / Yard Operators and convert legs of their haulage to rail freight where profitable (bulk haulage / containterised etc). Can you help us look larger, bolder and more robust than we really are (two man show)?
Target Market(s)
Transport Industry
Industry/Entity Type
Business
Contact Information for Business Card
Card details for both N Pollard and S Pollard have been uploaded on the publisher files
Colors
Designer to choose colors to be used in the design.
Requirements
Must have
- Similar theme both sides of card
Should not have
- Black on one side white on the other

```html
<!DOCTYPE html>
<html lang="en">
<head>
<meta charset="utf-8">
<title>Railvane Business Cards</title>
<link href="https://fonts.googleapis.com/css2?family=Roboto:wght@400;500;700;900&display=swap" rel="stylesheet">
<style>
  :root {
    --page-bg: #d9d6d2;
    --card-black: #141414;
    --card-edge: #1d1d1d;
    --emboss-grey: #4a4a4a;
    --url-grey: #9a9a9a;
    --brand-teal: #3aa3a8;
    --title-gold: #e0a11b;
    --text-white: #f2f2f2;
    --divider: #6b6b6b;
  }
  * { box-sizing: border-box; margin: 0; padding: 0; }
  html, body { width: 1200px; height: 864px; overflow: hidden; }
  body {
    background: var(--page-bg);
    font-family: "Roboto", Arial, sans-serif;
    position: relative;
  }
  .card {
    position: absolute;
    top: 278px;
    width: 540px;
    height: 308px;
    background: var(--card-black);
    border: 1px solid var(--card-edge);
    box-shadow: 0 10px 28px rgba(0,0,0,0.28);
  }
  .card--back { left: 40px; }
  .card--front { left: 620px; }

  .back-brand {
    position: absolute;
    left: 0; right: 0; top: 104px;
    text-align: center;
    font-weight: 900;
    font-size: 64px;
    letter-spacing: -1px;
    color: var(--emboss-grey);
  }
  .back-url {
    position: absolute;
    left: 0; right: 0; top: 206px;
    text-align: center;
    font-size: 14px;
    letter-spacing: 6px;
    color: var(--url-grey);
  }

  .front-brand {
    position: absolute;
    left: 34px; top: 122px;
    display: flex; align-items: center; gap: 10px;
  }
  .front-brand__mark {
    width: 14px; height: 14px; border-radius: 50%;
    background: var(--brand-teal);
  }
  .front-brand__name {
    font-weight: 900;
    font-size: 46px;
    letter-spacing: -1px;
    color: var(--brand-teal);
  }
  .divider {
    position: absolute;
    left: 300px; top: 40px;
    width: 1px; height: 228px;
    background: linear-gradient(to bottom, transparent, var(--divider) 20%, var(--divider) 80%, transparent);
  }
  .contact {
    position: absolute;
    left: 320px; top: 52px;
    color: var(--text-white);
  }
  .contact__name {
    font-weight: 500; font-size: 20px; color: var(--brand-teal);
  }
  .contact__title {
    font-size: 15px; color: var(--title-gold); margin-bottom: 10px;
  }
  .contact__address {
    font-size: 13.5px; line-height: 18px; margin-bottom: 8px;
  }
  .contact__list { list-style: none; font-size: 13.5px; }
  .contact__list li {
    display: flex; align-items: center; gap: 8px; height: 20px;
  }
  .contact__list svg { width: 12px; height: 12px; fill: var(--brand-teal); flex: none; }
</style>
</head>
<body>
  <section class="card card--back">
    <div class="back-brand">Railvane</div>
    <div class="back-url">www.railvane.net</div>
  </section>

  <section class="card card--front">
    <div class="front-brand">
      <span class="front-brand__mark"></span>
      <span class="front-brand__name">Railvane</span>
    </div>
    <div class="divider"></div>
    <div class="contact">
      <div class="contact__name">Neil Pollard</div>
      <div class="contact__title">President</div>
      <div class="contact__address">4127 Harbour Lane<br>Millbrook, NY 12545</div>
      <ul class="contact__list">
        <li><svg viewBox="0 0 12 12"><path d="M1 3c0-1 1-2 2.5-2h5C10 1 11 2 11 3v1H8V3H4v1H1zM2 5h8l1 6H1z"/></svg>555 0142 7781</li>
        <li><svg viewBox="0 0 12 12"><path d="M3 0h6a1 1 0 0 1 1 1v10a1 1 0 0 1-1 1H3a1 1 0 0 1-1-1V1a1 1 0 0 1 1-1zm0 2v8h6V2z"/></svg>555 0198 3364</li>
        <li><svg viewBox="0 0 12 12"><path d="M3 0h6v3H3zM1 4h10v5H9v3H3V9H1zm3 4v3h4V8z"/></svg>555 0176 2209</li>
        <li><svg viewBox="0 0 12 12"><path d="M0 2h12v1L6 7 0 3zm0 2.5 6 4 6-4V10H0z"/></svg>neil@railvane.net</li>
        <li><svg viewBox="0 0 12 12"><circle cx="6" cy="6" r="6"/></svg>www.railvane.net</li>
      </ul>
    </div>
  </section>
</body>
</html>
```